The calm within me tour 2019

I need an improvement of my own design for a speaking tour on shame and mental health. The advertisement will be for social media. I would like someone to remove the background and do something creative and contemporary. My preference is just my head and shoulders.

Target Market(s)

Church pastors and leaders of mental health organisations

Industry/Entity Type

Mental Health

Requirements
Must have
• The same wording as original
• Delete background and replace with something that is simple but funky

```html
<!DOCTYPE html>
<html lang="en">
<head>
<meta charset="utf-8">
<title>The Calm Within Me Tour 2019</title>
<link rel="stylesheet" href="https://fonts.googleapis.com/css2?family=Playfair+Display:wght@700;800&family=Titillium+Web:wght@400&display=swap">
<style>
  :root {
    --paper: #ffffff;
    --accent-blue: #5b7cf5;
    --accent-blue-soft: rgba(91, 124, 245, 0.55);
    --badge-light: #757575;
    --badge-dark: #565656;
    --badge-edge: #3a3a3a;
    --badge-text: #ffffff;
    --portrait-top: #8c7466;
    --portrait-mid: #6b5548;
    --portrait-base: #18181c;
  }

  * { margin: 0; padding: 0; box-sizing: border-box; }

  html, body {
    width: 1200px;
    height: 564px;
    overflow: hidden;
    background: var(--paper);
  }

  .tour-banner {
    position: relative;
    width: 1200px;
    height: 564px;
    overflow: hidden;
    background: var(--paper);
  }

  .backdrop-pattern {
    position: absolute;
    inset: 0;
    background:
      radial-gradient(ellipse 560px 330px at 960px 90px, var(--accent-blue) 0%, var(--accent-blue-soft) 45%, rgba(91,124,245,0.12) 75%, rgba(91,124,245,0) 100%),
      radial-gradient(ellipse 260px 160px at 1200px 200px, var(--accent-blue-soft) 0%, rgba(91,124,245,0) 100%),
      radial-gradient(ellipse 200px 150px at 0px 564px, rgba(91,124,245,0.45) 0%, rgba(91,124,245,0) 100%);
  }

  .tour-badge {
    position: absolute;
    left: 86px;
    top: 142px;
    width: 410px;
    height: 410px;
    border-radius: 50%;
    background: radial-gradient(circle at 40% 30%, var(--badge-light) 0%, var(--badge-dark) 100%);
    border: 1.5px solid var(--badge-edge);
    display: flex;
    flex-direction: column;
    align-items: center;
    justify-content: center;
    color: var(--badge-text);
    font-family: "Playfair Display", "Bodoni 72", Georgia, serif;
    font-weight: 700;
    text-align: center;
    line-height: 0.9;
  }

  .tour-badge__lead   { font-size: 46px; margin-left: 40px; }
  .tour-badge__word   { font-size: 86px; }
  .tour-badge__phrase { font-size: 66px; margin-top: 4px; }
  .tour-badge__year   { font-size: 118px; margin-top: 8px; font-weight: 800; }

  .speaker-name {
    position: absolute;
    left: 540px;
    top: 490px;
    width: 160px;
    text-align: center;
    font-family: "Titillium Web", "Exo 2", Arial, sans-serif;
    font-weight: 400;
    font-size: 23px;
    letter-spacing: 0.5px;
    color: var(--accent-blue);
  }

  .speaker-portrait {
    position: absolute;
    left: 776px;
    top: 36px;
    width: 412px;
    height: 528px;
    border-radius: 150px 150px 40px 40px;
    background: linear-gradient(180deg, var(--portrait-top) 0%, var(--portrait-mid) 45%, var(--portrait-base) 62%, var(--portrait-base) 100%);
  }
</style>
</head>
<body>
  <main class="tour-banner">
    <div class="backdrop-pattern" role="img" aria-label="Scattered blue triangle pattern, dense at top right and fading toward the centre and lower left"></div>

    <section class="tour-badge" aria-label="The Calm within me 2019">
      <span class="tour-badge__lead">The</span>
      <span class="tour-badge__word">Calm</span>
      <span class="tour-badge__phrase">within me</span>
      <span class="tour-badge__year">2019</span>
    </section>

    <p class="speaker-name">lena hart</p>

    <div class="speaker-portrait" role="img" aria-label="Head-and-shoulders photo of the speaker in a black V-neck t-shirt"></div>
  </main>
</body>
</html>
```